Need Professional, Modern, Clean Newsletter Templates for High End Real Estate Agents in Orange Coun

I need a newsletter for realtors who specialize in high-end home sales for Orange County, California. Please see the attached draft of the newsletter we have in mind. Please note the logo at the top and the beach imagery and please use these and complementary fonts, colors and themes when creating your design. These particular realtors focus on very high-end clients with a specialization on ocean front properties. I WANT YOU TO PLEASE USE THE HEADER FROM MY ATTACHMENT IN YOUR NEWSLETTER. THIS NEWSLETTER IS INTENDED TO BE SENT OUT VIA EMAIL ONLY, NOT PRINT.

The idea behind the newsletter is that it will cover four broad categories. We will have a content creator who will pull content each week, however we need a nice looking template that can support their content. These are the four categories :

1) Market Data - this will pull graphs and information that the realtors receive, directly from the MLS (home listing site). Most of this will be in graph or table form, so we need a nice way to support that.

2.) Featured Listings - this will show the featured homes they have for sale at any given time. This section of the template should have a place to put pictures of the home with supporting text.

3.) News you can use - links to videos and articles relevant to the real estate industry and in the area.

4.) Upcoming OC Events - list of upcoming events in the area.
Updates

I feel like I need to post this update in case there was some confusion in my contest brief.

I DO NOT want a new logo or header design. What I am looking for is a newsletter to support the header and logo I already have, and for a nice template which includes each of the four sections I described in my brief. I would like you to think about each of the four sections and design them accordingly. There needs to be a good section for graphs (market data), for videos, for featured listings (pictures of homes with supporting descriptive text) and upcoming events (maybe supported by a calendar and text sections to describe the event, etc.)

This newsletter will be sent out as email only. Your entries should be made as .pdf or as a word document. Thanks.

Target Market(s)

High end real estate buyers and sellers, with a focus on ocean front property.

Industry/Entity Type

Real Estate

Colors
33a6d7
00a990
86cae6

Requirements
Must have
• You MUST include the header photo from the .png attachment I included. "Varnell at the Shore - Sell with the Best."

```html
<!DOCTYPE html>
<html lang="en">
<head>
<meta charset="utf-8">
<title>Varnell at the Shore – January 2014 Newsletter</title>
<link href="https://fonts.googleapis.com/css2?family=Open+Sans:wght@300;400;600;700&display=swap" rel="stylesheet">
<style>
:root{
  --blue:#33a6d7;
  --blue-light:#86cae6;
  --teal:#00a990;
  --dark:#3a3a3a;
  --text:#555;
  --muted:#8a8a8a;
  --line:#d9d9d9;
  --panel:#f4f1f3;
  --red:#d9534f;
}
*{box-sizing:border-box;margin:0;padding:0}
html,body{width:1200px;height:4762px;overflow:hidden;background:#fff}
body{font-family:"Open Sans",Arial,sans-serif;color:var(--text);font-size:13px;line-height:1.5;position:relative}
a{color:var(--blue);text-decoration:none}

/* header */
.hero{height:300px;position:relative;background:linear-gradient(180deg,#2f9ed4 0%,#5fb9e2 35%,#9fd6ea 55%,#3fb3c7 62%,#e9eef0 80%,#fff 100%)}
.hero-logo{position:absolute;left:120px;top:30px;width:140px;height:110px;background:rgba(255,255,255,.85);border:2px solid var(--blue);display:flex;align-items:center;justify-content:center;text-align:center;padding:10px;color:var(--blue);font-size:19px;font-weight:600;line-height:1.2}
.hero-title{position:absolute;left:520px;top:168px;width:600px;text-align:center;color:#fff}
.hero-title h1{font-weight:300;font-size:40px;letter-spacing:2px;line-height:1.1}
.hero-title p{font-size:19px;font-weight:300;color:#e8f6fb;margin-top:4px}

.page{width:970px;margin-left:120px}

/* intro */
.intro{display:flex;gap:24px;height:760px}
.intro-main{width:700px}
.agent{float:left;width:140px;margin:10px 14px 6px 0;text-align:center}
.agent-photo{height:180px;background:linear-gradient(160deg,#9aa7b2,#4c5560)}
.agent-name{background:var(--blue);color:#fff;font-weight:700;font-size:12px;padding:4px 0}
.agent a{display:block;font-size:12px;margin-top:4px}
.issue-title{color:var(--blue);font-weight:400;font-size:21px;margin-top:6px}
.intro p{font-size:12px;margin-bottom:10px}
.quick-head{font-weight:700;color:#444;font-size:13px;margin:16px 0 8px}
.quick{list-style:none}
.quick li{margin-bottom:8px}
.quick a{font-size:21px;color:var(--blue);line-height:1.2}
.quick a::before{content:"• "}
.quick span{display:block;font-size:11px;color:#999;padding-left:12px;width:290px}

/* sidebar */
.sidebar{width:230px;padding-top:10px}
.box{border:1px solid var(--line);margin-bottom:24px;background:#fff}
.box-head{background:var(--blue);color:#fff;font-weight:600;padding:6px 10px;font-size:13px}
.menu .box-head{text-align:center;font-size:17px;font-weight:700}
.menu ul{list-style:none;padding:8px 14px}
.menu li{font-size:11px;font-weight:600;color:#444;display:flex;align-items:center;gap:8px;padding:5px 0}
.menu li::before{content:"";width:10px;height:10px;border-radius:50%;border:2px solid var(--blue)}
.signup{padding:10px}
.signup p{font-size:10px;color:#777}
.signup .field{border:1px solid #ccc;height:22px;margin:8px 0;font-size:10px;padding:3px 6px;color:#999}
.signup .btn{background:var(--red);color:#fff;text-align:center;font-size:11px;padding:3px}
.signup-links{font-size:10px;padding:0 10px 10px}
.posts{list-style:none;padding:8px 10px}
.posts li{border-bottom:1px solid #eee;padding:6px 0;font-size:10px;line-height:1.3}
.posts small{display:block;color:#aaa;font-size:9px}
.view-all{font-size:10px;padding:8px 10px;color:var(--red)}

/* section bands */
.band{background:var(--dark);color:#fff;height:48px;display:flex;align-items:center;padding:0 14px;gap:10px}
.band h2{font-weight:400;font-size:26px;color:#fff}
.band h2 em{font-style:normal;color:var(--blue)}
.band span{font-size:11px;color:#ddd}
.lead{font-size:12px;margin:14px 0}
.divider{border-top:6px solid var(--dark);margin:40px 0 24px}

/* market table */
.table-title{text-align:center;font-size:17px;color:#444;margin:16px 0 10px}
.market{margin:0 auto;width:890px;border-collapse:collapse;font-size:15px;border:1px solid #bbb}
.market th,.market td{padding:3px 10px;text-align:center;color:#222}
.market th:first-child,.market td:first-child{text-align:right;width:230px}
.market thead th{background:#e4eef5;font-weight:700;color:#1c4f8c}
.market tbody tr:nth-child(even){background:#f5f5f5}
.market a{text-decoration:underline;color:#1c5fab}

/* featured */
.featured{display:flex;gap:40px;margin-top:20px;height:400px}
.listing h3{font-weight:400;font-size:19px;color:#333}
.listing .city{font-size:13px}
.listing .price{font-size:24px;font-weight:600;color:#333;margin:18px 0 14px}
.listing p{font-size:14px;line-height:1.45}
.listing a{display:block;margin-top:20px;font-size:16px}

/* news */
.news-panel{background:var(--panel);padding:36px 30px 30px;height:1000px}
.tabs{display:flex;width:900px;margin:0 auto 20px}
.tab{flex:1;text-align:center;color:#fff;font-size:17px;padding:6px 0;background:#8a8a8a}
.tab.active{background:var(--blue)}
.article{display:flex;gap:14px;background:#fff;width:900px;margin:0 auto 16px;padding:12px;height:220px}
.article-img{width:155px;height:120px;flex:none;background:linear-gradient(180deg,#8cc7e8,#d9c9a8 55%,#6b8f5e)}
.article-body{flex:1;position:relative;font-size:12px}
.article h3{font-size:13px;font-weight:700;color:#222;margin-bottom:6px}
.article .meta{position:absolute;left:0;bottom:4px;font-size:11px;color:#888}
.article .more{position:absolute;right:0;bottom:4px;font-size:11px}
.chart-thumb{width:155px;height:120px;flex:none;background:#fff;border:1px solid #ddd}

/* events */
.events{list-style:none;margin-top:10px}
.events li{font-size:12px;padding:8px 0 8px 16px;border-bottom:1px dotted #ccc;position:relative}
.events li::before{content:"";position:absolute;left:2px;top:15px;width:6px;height:6px;background:var(--blue)}
.events a{text-decoration:underline}

/* footer */
.footer{display:flex;gap:40px;border-top:1px solid var(--line);padding-top:24px;margin-top:70px;height:240px}
.footer h4{font-size:14px;color:#444;font-weight:600;margin-bottom:10px;letter-spacing:.5px}
.about{width:300px}
.about-row{display:flex;gap:10px;font-size:10px}
.foot-logo{width:90px;height:70px;flex:none;border:2px solid var(--blue);color:var(--blue);font-weight:600;font-size:13px;display:flex;align-items:center;justify-content:center;text-align:center;line-height:1.2}
.contact{width:300px;font-size:12px}
.contact b{color:#444}
.follow ul{list-style:none}
.follow li{display:flex;align-items:center;gap:10px;font-size:12px;margin-bottom:8px}
.follow li::before{content:"";width:24px;height:24px;border-radius:50%;background:#777}
.unsub{font-size:11px;margin-top:30px}
.copyright{position:absolute;left:120px;bottom:40px;width:970px;background:var(--blue);color:#fff;text-align:center;font-size:11px;padding:8px 0}
</style>
</head>
<body>

<header class="hero" role="img" aria-label="Tropical beach with turquoise water and white sand under a blue sky">
  <div class="hero-logo">Varnell at the Shore</div>
  <div class="hero-title">
    <h1>SELL WITH THE BEST</h1>
    <p>Integer luctus odio tempor dui malesuada.</p>
  </div>
</header>

<main class="page">

  <section class="intro">
    <div class="intro-main">
      <div class="agent">
        <div class="agent-photo" role="img" aria-label="Portrait of the agent in a suit"></div>
        <div class="agent-name">REID HALSTON</div>
        <a href="#">E-mail</a>
      </div>
      <h2 class="issue-title">Jan 2014 Newsletter</h2>
      <p>Integer luctus odio tempor dui malesuada, et cursus justo accumsan. Class aptent taciti sociosqu ad litora torquent per conubia nostra, per inceptos himenaeos. Nullam id erat elit. Vivamus id tincidunt justo. Maecenas ipsum metus, lacinia vitae libero at, posuere egestas nisi. Sed convallis, massa in mollis fermentum, elit nulla laoreet tellus, non sodales risus lacus eu elit. Mauris sed vestibulum diam. Mauris sed vestibulum diam. Lorem ipsum dolor sit amet, consectetur adipiscing elit. Integer euismod turpis non gravida facilisis. Phasellus elementum pellentesque aliquet. Nullam sodales urna erat.</p>
      <p>Sed iaculis rhoncus dolor. Integer vel arcu nec elit varius dapibus ac nec mi. Vestibulum at nulla nec nulla pharetra sollicitudin. Nunc id libero vitae dui ultrices convallis. Maecenas nec facilisis mi. Mauris accumsan dui eu purus sodales pellentesque. Interdum et malesuada fames ac ante ipsum primis in faucibus. Nullam faucibus congue justo vel facilisis. Etiam quis ultricies libero, vitae tincidunt mauris. Etiam bibendum nisl non ante laoreet, in vulputate ligula venenatis. Quisque tincidunt eleifend orci. Praesent blandit ipsum sed purus tempor, at sagittis justo luctus. Sed a nisl orci. Duis tincidunt sapien id leo auctor convallis.</p>
      <p>Sed bibendum aliquet sem, in congue libero bibendum posuere. Cras lacus ipsum, venenatis vitae lacus nec, laoreet pulvinar nibh. Nam condimentum elit et libero luctus, sed pulvinar sapien fermentum. Nulla vitae lorem ut lacus vulputate lacinia. Suspendisse et massa cursus, mattis turpis et, varius augue. Integer sed leo eros. Nulla neque metus, pulvinar et nisl non, blandit cursus arcu. Nulla nec odio velit.</p>
      <p class="quick-head">Find below quick links to each segment of our newsletter:</p>
      <ul class="quick">
        <li><a href="#">Real Estate Market Data</a><span>Track monthly changes in property values and market trends</span></li>
        <li><a href="#">Featured Property Listings</a><span>Some of the best properties presently available for sale in OC</span></li>
        <li><a href="#">News You Can Use</a><span>Follow the latest news and issues impacting the real estate market</span></li>
        <li><a href="#">OC Community Events</a><span>Upcoming events of note in the Orange County community</span></li>
      </ul>
      <p style="margin-top:10px">We will be updating each section regularly every month, as well as adding new content every time. If you have any feedback, questions or comments please feel free to call or email. Thank you for your support and interest.</p>
    </div>

    <aside class="sidebar">
      <div class="box menu">
        <div class="box-head">MENU</div>
        <ul>
          <li>MARKET DATA</li>
          <li>FEATURED LISTINGS</li>
          <li>REAL ESTATE NEWS</li>
          <li>OC EVENTS</li>
        </ul>
      </div>
      <div class="box">
        <div class="box-head">NewsLetter</div>
        <div class="signup">
          <p>Get new listing alerts and market updates by email</p>
          <div class="field">E-mail</div>
          <div class="btn">Subscribe</div>
        </div>
        <div class="signup-links"><a href="#">» View Newsletter</a><br><a href="#">» Privacy Policy</a></div>
      </div>
      <div class="box">
        <div class="box-head">Blog Post</div>
        <ul class="posts">
          <li><a href="#">Coastal home values keep climbing along the shore</a><small>January 8, 2014</small></li>
          <li><a href="#">What buyers look for in an oceanfront estate today</a><small>January 6, 2014</small></li>
          <li><a href="#">Five questions to ask before you list your home</a><small>January 3, 2014</small></li>
          <li><a href="#">Inventory tightens across south county zip codes</a><small>December 30, 2013</small></li>
          <li><a href="#">Staging tips that help luxury homes sell faster</a><small>December 26, 2013</small></li>
          <li><a href="#">Year in review: the local luxury market in 2013</a><small>December 20, 2013</small></li>
          <li><a href="#">How mortgage rates shape high end demand</a><small>December 16, 2013</small></li>
          <li><a href="#">Bluff top living and what it really costs</a><small>December 12, 2013</small></li>
        </ul>
        <div class="view-all">» View All Posts</div>
      </div>
    </aside>
  </section>

  <section class="market-data">
    <div class="band"><h2><em>Market</em> Data</h2><span>Properly value a property for purchase or sale.</span></div>
    <p class="lead">Find below a compilation of key real estate market indicators for selected zip codes within Southern California. To properly value a property for purchase or sale, one must consider the broader market context and trendlines.</p>
    <h3 class="table-title">December 2013</h3>
    <table class="market">
      <thead><tr><th>Zip Code:</th><th>92677</th><th>92651</th><th>92672</th><th>92673</th><th>92629</th></tr></thead>
      <tbody>
        <tr><td>Monthly Units Sold</td><td>115</td><td>116</td><td>117</td><td>118</td><td>119</td></tr>
        <tr><td>Avg. Sold Price</td><td>$583K</td><td>$583K</td><td>$583K</td><td>$583K</td><td>$583K</td></tr>
        <tr><td>Sold % of Orig List $</td><td>95.5%</td><td>95.5%</td><td>95.5%</td><td>95.5%</td><td>95.5%</td></tr>
        <tr><td>Current Units Listed</td><td>122</td><td>122</td><td>122</td><td>122</td><td>122</td></tr>
        <tr><td>Avg. List Price</td><td>$1,415K</td><td>$1,415K</td><td>$1,415K</td><td>$1,415K</td><td>$1,415K</td></tr>
        <tr><td>Avg. Days on Market</td><td>83</td><td>83</td><td>83</td><td>83</td><td>83</td></tr>
        <tr><td>Historical Trends</td>
          <td><svg width="30" height="22" aria-hidden="true"><rect x="2" y="10" width="6" height="12" fill="#1c5fab"/><rect x="12" y="5" width="6" height="17" fill="#1c5fab"/><rect x="22" y="0" width="6" height="22" fill="#1c5fab"/></svg><br><a href="#">see charts</a></td>
          <td><svg width="30" height="22" aria-hidden="true"><rect x="2" y="10" width="6" height="12" fill="#1c5fab"/><rect x="12" y="5" width="6" height="17" fill="#1c5fab"/><rect x="22" y="0" width="6" height="22" fill="#1c5fab"/></svg><br><a href="#">see charts</a></td>
          <td><svg width="30" height="22" aria-hidden="true"><rect x="2" y="10" width="6" height="12" fill="#1c5fab"/><rect x="12" y="5" width="6" height="17" fill="#1c5fab"/><rect x="22" y="0" width="6" height="22" fill="#1c5fab"/></svg><br><a href="#">see charts</a></td>
          <td><svg width="30" height="22" aria-hidden="true"><rect x="2" y="10" width="6" height="12" fill="#1c5fab"/><rect x="12" y="5" width="6" height="17" fill="#1c5fab"/><rect x="22" y="0" width="6" height="22" fill="#1c5fab"/></svg><br><a href="#">see charts</a></td>
          <td><svg width="30" height="22" aria-hidden="true"><rect x="2" y="10" width="6" height="12" fill="#1c5fab"/><rect x="12" y="5" width="6" height="17" fill="#1c5fab"/><rect x="22" y="0" width="6" height="22" fill="#1c5fab"/></svg><br><a href="#">see charts</a></td>
        </tr>
      </tbody>
    </table>
  </section>

  <div class="divider"></div>

  <section class="featured-listings">
    <div class="band"><h2><em>Featured</em> Listings</h2><span>Some of the finest homes currently available for sale in the Orange County area.</span></div>
    <p class="lead">The following is a compilation of some of the finest homes currently available for sale in the Orange County area. If you are interested in any of these listings, please feel free to call or e-mail for additional information.</p>
    <div class="featured">
      <svg width="430" height="330" viewBox="0 0 430 330" role="img" aria-label="Bar chart of average sold price in thousands, October 2012 to September 2013" font-family="Open Sans, sans-serif" font-size="10" fill="#444">
        <rect x="0" y="0" width="430" height="330" fill="#fff" stroke="#ccc"/>
        <g stroke="#e3e3e3">
          <line x1="40" y1="20" x2="420" y2="20"/><line x1="40" y1="50" x2="420" y2="50"/><line x1="40" y1="80" x2="420" y2="80"/><line x1="40" y1="110" x2="420" y2="110"/><line x1="40" y1="140" x2="420" y2="140"/><line x1="40" y1="170" x2="420" y2="170"/><line x1="40" y1="200" x2="420" y2="200"/><line x1="40" y1="230" x2="420" y2="230"/><line x1="40" y1="260" x2="420" y2="260"/>
        </g>
        <line x1="40" y1="290" x2="420" y2="290" stroke="#888"/>
        <g text-anchor="end">
          <text x="34" y="24">900</text><text x="34" y="54">800</text><text x="34" y="84">700</text><text x="34" y="114">600</text><text x="34" y="144">500</text><text x="34" y="174">400</text><text x="34" y="204">300</text><text x="34" y="234">200</text><text x="34" y="264">100</text><text x="34" y="294">0</text>
        </g>
        <g fill="#2ab0c5">
          <rect x="48" y="115" width="20" height="175"/><rect x="79" y="84" width="20" height="206"/><rect x="110" y="86" width="20" height="204"/><rect x="141" y="93" width="20" height="197"/><rect x="172" y="96" width="20" height="194"/><rect x="203" y="108" width="20" height="182"/><rect x="234" y="70" width="20" height="220"/><rect x="265" y="43" width="20" height="247"/><rect x="296" y="82" width="20" height="208"/><rect x="327" y="72" width="20" height="218"/><rect x="358" y="78" width="20" height="212"/><rect x="389" y="70" width="20" height="220"/>
        </g>
        <g text-anchor="middle" font-weight="600" font-size="9">
          <text x="58" y="110">583</text><text x="89" y="79">686</text><text x="120" y="81">680</text><text x="151" y="88">656</text><text x="182" y="91">646</text><text x="213" y="103">605</text><text x="244" y="65">734</text><text x="275" y="38">824</text><text x="306" y="77">693</text><text x="337" y="67">728</text><text x="368" y="73">708</text><text x="399" y="65">735</text>
        </g>
        <g text-anchor="end" font-size="9">
          <text transform="translate(62 300) rotate(-45)">Oct-12</text><text transform="translate(93 300) rotate(-45)">Nov-12</text><text transform="translate(124 300) rotate(-45)">Dec-12</text><text transform="translate(155 300) rotate(-45)">Jan-13</text><text transform="translate(186 300) rotate(-45)">Feb-13</text><text transform="translate(217 300) rotate(-45)">Mar-13</text><text transform="translate(248 300) rotate(-45)">Apr-13</text><text transform="translate(279 300) rotate(-45)">May-13</text><text transform="translate(310 300) rotate(-45)">Jun-13</text><text transform="translate(341 300) rotate(-45)">Jul-13</text><text transform="translate(372 300) rotate(-45)">Aug-13</text><text transform="translate(403 300) rotate(-45)">Sep-13</text>
        </g>
      </svg>
      <div class="listing">
        <h3>18 Tidewater Lane</h3>
        <div class="city">Laguna Niguel, CA 92677</div>
        <div class="price">$489,900</div>
        <p>Bedrooms: 2 beds<br>Bathrooms: 2 full<br>Sq. Footage: 1,200<br>MLS# OC13245720</p>
        <a href="#">View Listing Details</a>
      </div>
    </div>
  </section>

  <div class="divider"></div>

  <section class="news">
    <div class="band"><h2><em>News</em> You Can Use</h2><span>National and local real estate issues</span></div>
    <p class="lead">Top news articles from this past month which cover national and local real estate issues and trends.</p>
    <div class="news-panel">
      <div class="tabs"><div class="tab active">Most Viewed</div><div class="tab">Recently Viewed</div></div>

      <article class="article">
        <div class="article-img" role="img" aria-label="Mediterranean style estate with palm trees"></div>
        <div class="article-body">
          <h3>We have recently had two substantial sales</h3>
          <p>In the local area which will close in the next two weeks," he said. "During my 40 years dealing with the mega houses of the cove and neighboring coastal bay, I have never seen as much interest from both international buyers and North American buyers as we are witnessing today."</p>
          <span class="meta">Dec, 31</span><a class="more" href="#">Read More...</a>
        </div>
      </article>
      <article class="article">
        <div class="article-img" role="img" aria-label="Hillside villa with terraced gardens"></div>
        <div class="article-body">
          <h3>We have recently had two substantial sales</h3>
          <p>In the local area which will close in the next two weeks," he said. "During my 40 years dealing with the mega houses of the cove and neighboring coastal bay, I have never seen as much interest from both international buyers and North American buyers as we are witnessing today."</p>
          <span class="meta">Dec, 31</span><a class="more" href="#">Read More...</a>
        </div>
      </article>
      <article class="article">
        <div class="article-img" role="img" aria-label="Luxury home with tower and cypress trees"></div>
        <div class="article-body">
          <h3>We have recently had two substantial sales</h3>
          <p>In the local area which will close in the next two weeks," he said. "During my 40 years dealing with the mega houses of the cove and neighboring coastal bay, I have never seen as much interest from both international buyers and North American buyers as we are witnessing today."</p>
          <span class="meta">Dec, 31</span><a class="more" href="#">Read More...</a>
        </div>
      </article>
      <article class="article">
        <svg class="chart-thumb" viewBox="0 0 155 120" role="img" aria-label="Small bar chart of home sales by zip code">
          <line x1="12" y1="105" x2="148" y2="105" stroke="#999"/>
          <g fill="#33a6d7"><rect x="18" y="60" width="10" height="45"/><rect x="34" y="45" width="10" height="60"/><rect x="50" y="55" width="10" height="50"/><rect x="66" y="35" width="10" height="70"/><rect x="82" y="50" width="10" height="55"/><rect x="98" y="30" width="10" height="75"/><rect x="114" y="42" width="10" height="63"/><rect x="130" y="25" width="10" height="80"/></g>
        </svg>
        <div class="article-body">
          <h3>Report of resale data of single family residences and condos as well as new homes by zip code within Orange County</h3>
          <p>As banks compete for affluent borrowers, an additional has emerged in the mortgage market: rates on loans for pricier homes — jumbo mortgages — have dropped below those for smaller mortgages.</p>
          <span class="meta">Dec, 31</span><a class="more" href="#">Read More...</a>
        </div>
      </article>
    </div>
  </section>

  <section class="events-section" style="margin-top:50px">
    <div class="band"><h2><em>Upcoming</em> OC Events</h2><span>National and local real estate issues</span></div>
    <p class="lead">Top news articles from this past month which cover national and local real estate issues and trends.</p>
    <ul class="events">
      <li><a href="#">Harbor &amp; Lyle chief strategy officer, provides perspective on the housing market as pending</a></li>
      <li><a href="#">Harbor &amp; Lyle chief strategy officer, provides perspective on the housing market as pending</a></li>
      <li><a href="#">Harbor &amp; Lyle chief strategy officer, provides perspective on the housing market as pending</a></li>
      <li><a href="#">Harbor &amp; Lyle chief strategy officer, provides perspective on the housing market as pending</a></li>
      <li><a href="#">Harbor &amp; Lyle chief strategy officer, provides perspective on the housing market as pending</a></li>
      <li><a href="#">Harbor &amp; Lyle chief strategy officer, provides perspective on the housing market as pending</a></li>
      <li><a href="#">Harbor &amp; Lyle chief strategy officer, provides perspective on the housing market as pending</a></li>
      <li><a href="#">Harbor &amp; Lyle chief strategy officer, provides perspective on the housing market as pending</a></li>
    </ul>
  </section>

  <footer>
    <div class="footer">
      <div class="about">
        <h4>ABOUT</h4>
        <div class="about-row">
          <div class="foot-logo">Varnell at the Shore</div>
          <p>Integer luctus odio tempor dui malesuada, et cursus justo accumsan. Class aptent taciti sociosqu ad litora torquent per conubia nostra, per inceptos himenaeos.</p>
        </div>
        <p style="font-size:10px;margin-top:6px">Maecenas ipsum metus, lacinia vitae libero at, posuere egestas nisi. Sed convallis, massa in mollis fermentum, elit nulla laoreet tellus, non sodales risus lacus eu elit. Mauris sed vestibulum diam.</p>
      </div>
      <div class="contact">
        <h4>PERSONAL CONTACT</h4>
        <p><b>Our mailing address is:</b><br>VarnellShore.example<br>40 Marlin Point Road<br>Cove Harbor, CA 92600</p>
      </div>
      <div class="follow">
        <h4>FOLLOW US</h4>
        <ul><li>Social</li><li>Updates</li><li>Network</li><li>Circle</li></ul>
      </div>
    </div>
    <p class="unsub"><a href="#">unsubscribe from this list</a> | <a href="#">update subscription preferences</a></p>
  </footer>
</main>

<div class="copyright">Copyright © 2014 VarnellShore.example, All rights reserved.</div>
</body>
</html>
```